Halcyon Bus Card

i own a building in the bronx ny - its called "Halcyon 7 by 2 HDFC"i want a classy logo / business card - nothing too religuous but it is like a family there - its a large apartment building - colors i like dark red, black, medium shade of gray also reg business card stuff tel # 845-555-0172 address 3862 Larkmoor Ave Bronx NY 10471 Email fijosh@aol.comslogan - " from many we are one "i can send u a picture of the building for the backside

```html
<!DOCTYPE html>
<html lang="en">
<head>
<meta charset="UTF-8">
<title>Halcyon 7 by 2 HDFC — Business Card</title>
<link href="https://fonts.googleapis.com/css2?family=Jost:ital,wght@0,400;0,700;1,400&display=swap" rel="stylesheet">
<style>
  :root {
    --canvas-bg: #e5e5e5;
    --canvas-shade: #cccccc;
    --card-base: #1e1e1e;
    --card-panel: #333333;
    --card-facet: #242424;
    --card-facet-light: #2a2a2a;
    --back-base: #000000;
    --back-band: #1c1c1c;
    --red: #8b1a1a;
    --red-deep: #5e0d0d;
    --red-dark: #3e0707;
    --white: #ffffff;
  }
  * { margin: 0; padding: 0; box-sizing: border-box; }
  html, body { width: 1200px; height: 1200px; overflow: hidden; }
  body { background: var(--canvas-bg); position: relative; font-family: "Jost", sans-serif; }

  .backdrop-shade { position: absolute; inset: 0; width: 1200px; height: 1200px; }

  .card {
    position: absolute;
    left: 367px;
    width: 466px;
    height: 266px;
    overflow: hidden;
  }
  .card--front { top: 320px; }
  .card--back { top: 633px; }
  .card__art { position: absolute; inset: 0; width: 100%; height: 100%; }

  .holder-name {
    position: absolute; left: 105px; top: 22px;
    font-size: 27px; font-weight: 700; color: var(--white);
    line-height: 1; letter-spacing: 0.2px;
  }
  .holder-position {
    position: absolute; left: 110px; top: 48px;
    font-size: 16px; font-weight: 400; color: var(--red);
    line-height: 1;
  }
  .company-name {
    position: absolute; left: 222px; top: 166px;
    font-size: 21.5px; font-weight: 700; color: var(--white);
    line-height: 1; white-space: nowrap;
  }
  .contact-list {
    position: absolute; left: 226px; top: 199px;
    list-style: none;
  }
  .contact-list li {
    display: flex; align-items: center; gap: 8px;
    height: 13.5px;
    font-size: 10px; color: var(--white); line-height: 1; white-space: nowrap;
    letter-spacing: 0.2px;
  }
  .contact-list svg { width: 12px; height: 10px; flex: none; fill: var(--red); }

  .slogan {
    position: absolute; left: 0; right: 0; top: 122px;
    text-align: center;
    font-size: 16px; font-style: italic; font-weight: 400;
    color: var(--white); letter-spacing: 0.3px;
  }
</style>
</head>
<body>

<svg class="backdrop-shade" viewBox="0 0 1200 1200" aria-hidden="true">
  <polygon points="0,0 119,0 427,582 89,1200 0,1200" fill="var(--canvas-shade)"/>
</svg>

<section class="card card--front" aria-label="Business card front">
  <svg class="card__art" viewBox="0 0 579 330" preserveAspectRatio="none" aria-hidden="true">
    <rect width="579" height="330" fill="var(--card-base)"/>
    <polygon points="198,185 470,0 579,0 579,330 320,330" fill="var(--card-facet)"/>
    <polygon points="495,0 579,0 579,95" fill="var(--card-facet-light)"/>
    <polygon points="0,0 30,0 128,150 25,330 0,330" fill="var(--card-panel)"/>
    <polygon points="32,0 46,0 145,152 66,330 25,330 128,150" fill="var(--red)"/>
    <polygon points="32,0 38,0 134,151 36,330 25,330 126,150" fill="var(--red-deep)"/>
  </svg>

  <h1 class="holder-name">YOUR NAME</h1>
  <p class="holder-position">POSITION</p>

  <h2 class="company-name">Halcyon 7 by 2 HDFC</h2>
  <ul class="contact-list">
    <li>
      <svg viewBox="0 0 12 10" aria-hidden="true"><path d="M1 3.5C1 2 3 1 6 1s5 1 5 2.5L9 4.3V3.2H3v1.1L1 3.5zM3 4.5h6l1.5 4.5h-9z"/></svg>
      # 845-555-0172
    </li>
    <li>
      <svg viewBox="0 0 12 10" aria-hidden="true"><path d="M6 0.5L0.5 5h1.5v4.5h3V6.5h2v3h3V5h1.5z"/></svg>
      Larkmoor Ave Bronx NY 10471
    </li>
    <li>
      <svg viewBox="0 0 12 10" aria-hidden="true"><path d="M0.5 1h11v8h-11zM1.6 2.2v5.9h8.8V2.2L6 5.6z M2.4 2l3.6 2.8L9.6 2z"/></svg>
      kelmar@mailbrook.net
    </li>
  </ul>
</section>

<section class="card card--back" aria-label="Business card back">
  <svg class="card__art" viewBox="0 0 579 330" preserveAspectRatio="none" aria-hidden="true">
    <rect width="579" height="330" fill="var(--back-base)"/>
    <polygon points="200,0 579,0 579,72 505,92" fill="var(--back-band)"/>
    <polygon points="200,0 230,0 505,92 579,72 579,84 503,114" fill="var(--red-dark)"/>
    <polygon points="215,0 230,0 505,92 579,72 579,77 504,100" fill="var(--red-deep)"/>
  </svg>
  <p class="slogan">“ from many we are one "</p>
</section>

</body>
</html>
```